Company or website name
- www.HerbalCareOutlet.example
- Links to the website
- We are developing a nationwide databse of Medical Marijuana Providers
- Other Facts

```html
<!DOCTYPE html>
<html lang="en">
<head>
<meta charset="utf-8">
<title>Herbal Care – National Medical Marijuana Provider Search</title>
<link rel="stylesheet" href="https://fonts.googleapis.com/css2?family=Source+Sans+3:wght@400;600;700&family=Cinzel:wght@700&display=swap">
<style>
  :root {
    --header-grey: #e6e7e6;
    --band-green: #4d6b22;
    --band-line: #8aa55c;
    --leaf-green: #8ccf3a;
    --button-green: #7cc23f;
    --button-light: #d6f0b0;
    --page-grey: #a7a7a7;
    --stripe-grey: #9a9a9a;
    --panel-black: #050807;
    --panel-dark: #1a1d1b;
    --title-grey: #5a5a5a;
    --text-dark: #1c1c1c;
    --text-green: #8fd13a;
    --text-light: #e3e3e3;
    --media-dark: #333333;
    --media-yellow: #f5e800;
    --play-orange: #f7a518;
    --footer-grey: #e4e4e4;
    --white: #ffffff;
  }
  * { box-sizing: border-box; margin: 0; padding: 0; }
  html, body { width: 1200px; height: 900px; overflow: hidden; background: var(--white); }
  .page {
    position: relative; width: 1200px; height: 900px; overflow: hidden;
    font-family: "Source Sans 3", sans-serif; background: var(--page-grey);
  }

  /* Header */
  .header-top { position: absolute; left: 0; top: 0; width: 1200px; height: 92px; background: var(--header-grey); }
  .header-band {
    position: absolute; left: 0; top: 92px; width: 1200px; height: 52px;
    background: linear-gradient(to bottom, var(--band-line) 0 8px, #5f7f2c 8px, var(--band-green) 52px);
  }
  .header-rule { position: absolute; left: 0; top: 144px; width: 1200px; height: 12px; background: #c9c9c9; }
  .leaf {
    position: absolute;
    background: radial-gradient(ellipse at center, var(--leaf-green) 0%, rgba(140,207,58,0.75) 45%, rgba(140,207,58,0) 72%);
  }
  .leaf--left { left: 6px; top: 0; width: 170px; height: 170px; }
  .leaf--center { left: 527px; top: 0; width: 142px; height: 100px; }
  .leaf--right { left: 1010px; top: 0; width: 185px; height: 165px; }
  .site-address {
    position: absolute; left: 179px; top: 63px;
    font-size: 12px; font-weight: 700; color: var(--text-dark);
  }
  .brand-name {
    position: absolute; left: 470px; top: 50px; width: 244px; text-align: center;
    font-size: 40px; font-weight: 700; line-height: 48px; color: var(--text-dark);
  }
  .main-nav { position: absolute; top: 114px; left: 0; width: 1200px; height: 32px; }
  .nav-button {
    position: absolute; top: 0; width: 154px; height: 31px;
    border-radius: 5px 5px 0 0;
    background: linear-gradient(to bottom, var(--button-light) 0%, #a6dc6d 35%, var(--button-green) 100%);
    color: var(--text-dark); font-size: 16px; text-align: center; line-height: 31px; text-decoration: none;
  }
  .nav-button--home { left: 195px; }
  .nav-button--about { left: 413px; }
  .nav-button--search { left: 639px; }
  .nav-button--contact { left: 858px; }

  /* Left column */
  .sidebar { position: absolute; left: 0; top: 156px; width: 300px; height: 674px; background: var(--panel-black); }
  .sidebar-photo {
    position: absolute; left: 0; top: 0; width: 300px; height: 190px;
    background: radial-gradient(ellipse at 40% 40%, #3e5a2c 0%, #1f3018 55%, #0a120a 100%);
  }
  .compass-icon {
    position: absolute; left: 64px; top: 20px; width: 148px; height: 140px;
    background: radial-gradient(circle at center, #e9c84a 0 18%, #2f7a3c 19% 40%, rgba(47,122,60,0) 62%);
  }
  .sidebar-title {
    position: absolute; left: 0; top: 190px; width: 300px; height: 41px;
    background: linear-gradient(to bottom, #6d6d6d, var(--title-grey));
    font-family: "Cinzel", serif; font-size: 19px; color: var(--white);
    text-align: center; line-height: 41px; letter-spacing: 0.5px;
  }
  .search-panel {
    position: absolute; left: 9px; top: 231px; width: 282px; height: 419px; overflow: hidden;
    background: linear-gradient(to bottom, var(--panel-dark), #0b0d0c 40%, #000 100%);
  }
  .search-intro {
    position: absolute; left: 0; top: 34px; width: 282px; text-align: center;
    font-size: 13px; font-weight: 600; color: var(--text-light);
  }
  .search-label {
    position: absolute; left: 0; top: 88px; width: 282px; text-align: center;
    font-size: 13px; font-weight: 700; line-height: 16px; color: var(--white);
  }
  .search-field {
    position: absolute; left: 12px; top: 129px; width: 246px; height: 28px;
    border-radius: 14px; background: linear-gradient(to bottom, #fff, #e6e6e6);
  }
  .search-field svg { position: absolute; right: 10px; top: 3px; }
  .search-button {
    position: absolute; left: 100px; top: 164px; width: 73px; height: 28px;
    border-radius: 8px; background: linear-gradient(to bottom, #ffffff, #dcdcdc);
  }
  .search-button svg { position: absolute; right: 8px; top: 9px; }
  .map-globe {
    position: absolute; left: 12px; top: 206px; width: 270px; height: 270px; border-radius: 50%;
    background: radial-gradient(circle at 50% 45%, #5b7a52 0%, #2c4a28 45%, #0f1f0e 80%, #07120a 100%);
    box-shadow: 0 0 12px rgba(120,210,90,0.55);
  }

  /* Centre column */
  .content {
    position: absolute; left: 300px; top: 156px; width: 598px; height: 674px;
    background: repeating-linear-gradient(to bottom, #b1b1b1 0 3px, var(--stripe-grey) 3px 5px);
  }
  .media-player { position: absolute; left: 89px; top: 35px; width: 422px; height: 307px; background: var(--media-dark); }
  .media-bar {
    position: absolute; left: 0; width: 422px; height: 21px;
    background: linear-gradient(to right, #4fa82a 0%, #d8f3b5 10%, #8ed156 30%, #6cbf3b 70%, #3a8b1d 100%);
  }
  .media-bar--top { top: 0; }
  .media-bar--bottom { bottom: 0; }
  .media-label {
    position: absolute; left: 0; top: 103px; width: 422px; text-align: center;
    font-size: 12px; font-weight: 700; color: var(--media-yellow);
  }
  .play-button { position: absolute; left: 185px; top: 131px; }
  .body-copy {
    position: absolute; left: 82px; width: 450px;
    font-size: 12.8px; line-height: 17px; color: var(--text-dark);
  }
  .body-copy--first { top: 355px; }
  .body-copy--second { top: 525px; }

  /* Right column */
  .aside { position: absolute; left: 898px; top: 156px; width: 302px; height: 674px; background: var(--panel-black); }
  .aside-photo {
    position: absolute; left: 2px; top: 2px; width: 298px; height: 156px;
    background: linear-gradient(160deg, #cfd4cc 0%, #6f7d63 35%, #2f3b27 70%, #111 100%);
  }
  .aside-copy {
    position: absolute; left: 17px; width: 272px;
    font-size: 12.8px; font-weight: 600; line-height: 17px; color: var(--text-green);
  }
  .aside-copy--first { top: 160px; }
  .aside-copy--second { top: 398px; }

  /* Footer */
  .footer-band {
    position: absolute; left: 0; top: 830px; width: 1200px; height: 23px;
    background: linear-gradient(to right, #e9f5d9 0%, #9fd66a 12%, #6dbd3a 40%, #4f9e25 100%);
  }
  .footer { position: absolute; left: 0; top: 853px; width: 1200px; height: 47px; background: var(--footer-grey); }
  .footer-links {
    position: absolute; left: 0; top: 13px; width: 1200px; text-align: center;
    font-size: 12.5px; color: var(--text-dark); word-spacing: 2px;
  }
  .footer-links a { color: inherit; text-decoration: none; }
</style>
</head>
<body>
<div class="page">

  <header>
    <div class="header-top"></div>
    <div class="header-band"></div>
    <div class="header-rule"></div>
    <div class="leaf leaf--left" role="img" aria-label="Green leaf illustration"></div>
    <div class="leaf leaf--center" role="img" aria-label="Green leaf illustration"></div>
    <div class="leaf leaf--right" role="img" aria-label="Green leaf illustration"></div>
    <div class="site-address">www.HerbalCareOutlet.example</div>
    <div class="brand-name">Herbal Care</div>
    <nav class="main-nav">
      <a class="nav-button nav-button--home" href="#">Home</a>
      <a class="nav-button nav-button--about" href="#">About Us</a>
      <a class="nav-button nav-button--search" href="#">Search</a>
      <a class="nav-button nav-button--contact" href="#">Contact</a>
    </nav>
  </header>

  <aside class="sidebar">
    <div class="sidebar-photo" role="img" aria-label="Photo of cannabis plant foliage">
      <div class="compass-icon" role="img" aria-label="Compass star icon with leaf emblem and pointer"></div>
    </div>
    <h2 class="sidebar-title">National Search</h2>
    <div class="search-panel">
      <p class="search-intro">Search for Medical Marijuana near you</p>
      <p class="search-label">Search by<br>Zipcode or State</p>
      <div class="search-field">
        <svg width="24" height="22" viewBox="0 0 24 22" aria-hidden="true">
          <circle cx="14" cy="9" r="6.5" fill="none" stroke="#111" stroke-width="2"/>
          <line x1="9.5" y1="13.5" x2="2" y2="20" stroke="#111" stroke-width="3" stroke-linecap="round"/>
        </svg>
      </div>
      <div class="search-button">
        <svg width="8" height="10" viewBox="0 0 8 10" aria-hidden="true"><path d="M1 0 L7 5 L1 10 Z" fill="#f39a1e"/></svg>
      </div>
      <div class="map-globe" role="img" aria-label="Glowing globe with a map of the United States"></div>
    </div>
  </aside>

  <main class="content">
    <div class="media-player">
      <div class="media-bar media-bar--top"></div>
      <p class="media-label">Media goes here</p>
      <svg class="play-button" width="40" height="40" viewBox="0 0 40 40" aria-hidden="true">
        <defs>
          <linearGradient id="play-fill" x1="0" y1="0" x2="0" y2="1">
            <stop offset="0" stop-color="#ffd45a"/>
            <stop offset="1" stop-color="#f59512"/>
          </linearGradient>
        </defs>
        <rect x="1" y="1" width="38" height="38" rx="6" fill="url(#play-fill)" stroke="#b86a07" stroke-width="1"/>
        <path d="M14 10 L29 20 L14 30 Z" fill="#222"/>
      </svg>
      <div class="media-bar media-bar--bottom"></div>
    </div>
    <p class="body-copy body-copy--first">Lorem ipsum dolor sit amet, ullamcorper et lobortis pellentesque a vitae elit, vestibulum in volutpat, placerat id purus mus ante a. Ut in amet mauris suspendisse ut pede, ligula mi. Ut accumsan nunc nec cubilia nonummy varius, erat nunc class volutpat, blandit vivamus etiam purus odio gravida, leo in donec aenean amet. Pede in nulla etiam. Eu nec, arcu diam mauris vestibulum commodo. Nulla diam ac nullam magna quam cras, nulla amet turpis. Cum consectetuer, gravida luctus. Fusce sed risus augue, metus vivamus. Consequat maecenas malesuada sollicitudin sapien lacus ut, phasellus morbi aliquet eget</p>
    <p class="body-copy body-copy--second">Lorem ipsum dolor sit amet, ullamcorper et lobortis pellentesque a vitae elit, vestibulum in volutpat, placerat id purus mus ante a. Ut in amet mauris suspendisse ut pede, ligula mi. Ut accumsan nunc nec cubilia nonummy varius, erat nunc class volutpat, blandit vivamus etiam purus odio gravida, leo in donec aenean amet. Pede in nulla etiam. Eu nec, arcu diam mauris vestibulum commodo. Nulla diam ac nullam magna quam cras, nulla amet turpis. Cum consectetuer, gravida luctus. Fusce sed risus augue, metus vivamus. Consequat maecenas malesuada sollicitudin sapien lacus ut, phasellus morbi</p>
  </main>

  <aside class="aside">
    <div class="aside-photo" role="img" aria-label="Photo of young plants growing in pots under grow lights"></div>
    <p class="aside-copy aside-copy--first">Lorem ipsum dolor sit amet, vulputate magna sed neque rutrum neque nibh, phasellus massa, est nibh lobortis quam, hendrerit dolor, amet lorem. Maecenas odio a fringilla ligula eget. Vel pharetra varius natoque eros arcu, habitasse orci suscipit id, vitae feugiat lorem, nibh purus semper interdum consectetuer ipsum. Quibusdam id lacus dolor duis, fringilla donec mus velit, neque vitae a eget urna. Aliquam semper, ornare nulla, sed vivamus etiam cras, sit augue tellus, et leo ullamcorper curabitur</p>
    <p class="aside-copy aside-copy--second">Blandit justo pulvinar, praesent dui praesent, parturient felis wisi nulla eros eros, eget condimentum non. Curabitur ullamcorper, non suspendisse augue sed enim dignissim imperdiet, sed egestas feugiat ornare cras magna, curabitur necessitatibus vitae accumsan praesent. Ligula fringilla risus molestie sed nec nascetur, libero auctor magna sit ut vivamus. Vitae gravida felis adipiscing quam aliquam dui, metus mollis pulvinar arcu vel, turpis tellus lectus quis, magna velit urna ipsum. Sollicitudin torquent sed, mauris justo dictum commodo, ante enim sagittis urna egestas sem hendre-</p>
  </aside>

  <div class="footer-band"></div>
  <footer class="footer">
    <p class="footer-links">
      <a href="#">Home</a> &nbsp;| &nbsp;<a href="#">About</a> &nbsp;| &nbsp;<a href="#">Search</a> &nbsp;| &nbsp;<a href="#">Contact</a> &nbsp;| &nbsp;<a href="#">Resources</a> &nbsp;| &nbsp;<a href="#">Legal</a>
    </p>
  </footer>

</div>
</body>
</html>
```